Business Card Design Project

I have just chosen a logo and would now like this designed onto a business card for my hair salon. I would like it to be classy not to busy and have a wow factor when people look at them
Has to Include on card:
Logo Design
And business details below
Kellie-ann Drummond (owner)
0482 736 219
Rdw@vomblet.com.au
71 Willowmere Rise Corvin Cove
Logo is now attached please provide designs
Hair

```html
<!DOCTYPE html>
<html lang="en">
<head>
<meta charset="utf-8">
<title>Marlowe Hair Atelier – Business Card</title>
<link rel="stylesheet" href="https://fonts.googleapis.com/css2?family=Crimson+Text:wght@400;600&display=swap">
<style>
  :root {
    --stage: #1b1b1b;
    --card-dark: #141618;
    --card-dark-glow: #24282b;
    --card-light: #ffffff;
    --swirl-tone: #ececec;
    --rule-light: #6f7477;
    --brand: #e619d6;
    --ink: #1e1e1e;
    --muted: #6d6d6d;
    --dots: #555555;
  }
  * { margin: 0; padding: 0; box-sizing: border-box; }
  html, body { width: 1200px; height: 900px; overflow: hidden; }
  body {
    background: var(--stage);
    font-family: "Crimson Text", Georgia, serif;
    position: relative;
  }
  .card {
    position: absolute;
    left: 368px;
    width: 454px;
  }
  .card--front {
    top: 119px;
    height: 260px;
    background: radial-gradient(ellipse at 50% 45%, var(--card-dark-glow) 0%, var(--card-dark) 70%);
  }
  .card--back {
    top: 473px;
    height: 263px;
    background: var(--card-light);
    overflow: hidden;
  }
  .front-rule {
    position: absolute;
    left: 116px;
    width: 229px;
    height: 1px;
    background: var(--rule-light);
  }
  .front-rule--top { top: 79px; }
  .front-rule--bottom { top: 184px; }
  .brand-name {
    position: absolute;
    text-align: center;
    color: var(--brand);
    font-weight: 600;
    text-transform: uppercase;
    line-height: 1;
  }
  .brand-name__main { display: block; font-size: 33px; letter-spacing: 0.5px; }
  .brand-name__sub { display: block; font-size: 20px; letter-spacing: 0.5px; margin-top: 2px; }
  .card--front .brand-name { left: 0; width: 100%; top: 100px; }
  .card--back .brand-name { left: 30px; width: 180px; top: 102px; }
  .card--back .brand-name__main { font-size: 30px; }
  .card--back .brand-name__sub { font-size: 18px; }
  .hair-swirl {
    position: absolute;
    inset: 0;
    background:
      radial-gradient(ellipse 60% 90% at 15% 70%, var(--swirl-tone) 0%, transparent 60%),
      radial-gradient(ellipse 60% 90% at 85% 70%, var(--swirl-tone) 0%, transparent 60%),
      radial-gradient(ellipse 40% 50% at 50% 0%, var(--swirl-tone) 0%, transparent 70%);
    opacity: 0.7;
  }
  .divider {
    position: absolute;
    left: 226px;
    top: 76px;
    height: 106px;
    border-left: 1.5px dotted var(--dots);
  }
  .role {
    position: absolute;
    left: 279px;
    top: 84px;
    font-size: 11px;
    color: var(--muted);
    letter-spacing: 0.4px;
  }
  .person {
    position: absolute;
    left: 237px;
    top: 99px;
    font-size: 14.5px;
    color: var(--ink);
    text-transform: uppercase;
    letter-spacing: 0.6px;
  }
  .contacts {
    position: absolute;
    left: 237px;
    top: 131px;
    list-style: none;
  }
  .contacts li {
    display: flex;
    align-items: center;
    height: 14px;
    font-size: 9.5px;
    color: var(--muted);
  }
  .contacts svg { width: 9px; height: 9px; margin-right: 6px; fill: var(--ink); flex: none; }
  .contacts .email { text-transform: lowercase; }
</style>
</head>
<body>
  <section class="card card--front" aria-label="Card front">
    <div class="front-rule front-rule--top"></div>
    <h1 class="brand-name">
      <span class="brand-name__main">Marlowe</span>
      <span class="brand-name__sub">Hair Atelier</span>
    </h1>
    <div class="front-rule front-rule--bottom"></div>
  </section>

  <section class="card card--back" aria-label="Card back">
    <div class="hair-swirl" role="img" aria-label="Faint flowing hair swirl decoration in pale grey"></div>
    <h2 class="brand-name">
      <span class="brand-name__main">Marlowe</span>
      <span class="brand-name__sub">Hair Atelier</span>
    </h2>
    <div class="divider"></div>
    <p class="role">Salon Owner</p>
    <p class="person">Kellie-ann Drummond</p>
    <ul class="contacts">
      <li>
        <svg viewBox="0 0 10 10" aria-hidden="true"><rect x="2.5" y="0.5" width="5" height="9" rx="1"/><rect x="3.4" y="1.6" width="3.2" height="5.8" fill="#fff"/></svg>
        phone - 0482 736 219
      </li>
      <li>
        <svg viewBox="0 0 10 10" aria-hidden="true"><rect x="0.5" y="2" width="9" height="6.5"/><path d="M0.8 2.3 L5 5.6 L9.2 2.3" stroke="#fff" stroke-width="0.9" fill="none"/></svg>
        <span>e-mail - <span class="email">Rdw@vomblet.com.au</span></span>
      </li>
      <li>
        <svg viewBox="0 0 10 10" aria-hidden="true"><path d="M5 0.5 C2.6 0.5 1.3 2.2 1.3 4 C1.3 6.3 5 9.6 5 9.6 C5 9.6 8.7 6.3 8.7 4 C8.7 2.2 7.4 0.5 5 0.5 Z"/><circle cx="5" cy="3.9" r="1.3" fill="#fff"/></svg>
        address - 71 Willowmere Rise Corvin Cove
      </li>
    </ul>
  </section>
</body>
</html>
```